Velvet Bloom Marisol's Cleaning Service Business Cards Project

A business card with all contact details with logo design on there (already have a logo) eye catching Logo and contact info on one side, full logo on the back, must target upper class residential and corporate companies, fitness companies, still keep it on the feminine side of things , must look elegant

Target Market(s)

Upper class homes and corporate companies

Industry/Entity Type

Cleaning Service

Contact Information for Business Card

Name: Marisol Denhart
Position: Director
ABN: 47193062857
Email: marisolsvelvetcleaning@brightmail.example
Number: 0418926547

Font styles to use
Decorative

Colors

Designer to choose colors to be used in the design.

Requirements
Must have
• Available Sydney Wide, contact info and logo on one side, full logo on the back
Nice to have
• Professional appearance
Should not have
• Cheap advert looking stuff

```html
<!DOCTYPE html>
<html lang="en">
<head>
<meta charset="utf-8">
<title>Velvet Bloom Marisol's Cleaning Service – Business Cards</title>
<link href="https://fonts.googleapis.com/css2?family=Noto+Serif:wght@400;700&family=Roboto:wght@400&display=swap" rel="stylesheet">
<style>
  :root {
    --backdrop: #3b3b3b;
    --card: #262626;
    --silver: #c9c9c9;
    --teal: #5ec7ca;
    --white: #f2f2f2;
  }
  * { margin: 0; padding: 0; box-sizing: border-box; }
  html, body { width: 1200px; height: 900px; overflow: hidden; }
  body {
    background: var(--backdrop);
    display: flex;
    flex-direction: column;
    align-items: center;
    justify-content: center;
    gap: 36px;
  }
  .card {
    width: 720px;
    height: 400px;
    background: var(--card);
    display: flex;
    flex-direction: column;
    align-items: center;
    justify-content: center;
  }
  .brand-name {
    font-family: "Noto Serif", serif;
    font-weight: 400;
    color: var(--silver);
    text-align: center;
    margin-top: 150px;
  }
  .brand-name .title {
    display: block;
    font-size: 34px;
    letter-spacing: 2px;
    text-transform: uppercase;
  }
  .brand-name .tagline {
    display: block;
    font-size: 12px;
    letter-spacing: 5px;
    text-transform: uppercase;
    margin-top: 6px;
  }
  .contact-name {
    font-family: "Noto Serif", serif;
    font-weight: 700;
    font-size: 34px;
    color: var(--teal);
    letter-spacing: 1px;
  }
  .contact-role {
    font-family: "Roboto", sans-serif;
    font-size: 19px;
    color: var(--white);
    margin-top: 2px;
  }
  .divider {
    width: 50px;
    height: 2px;
    background: var(--white);
    margin: 22px 0 20px;
  }
  .contact-line {
    font-family: "Roboto", sans-serif;
    font-size: 20px;
    color: var(--white);
    display: flex;
    align-items: center;
    gap: 8px;
    line-height: 1.4;
  }
  .contact-line svg { width: 18px; height: 18px; flex: none; }
  .abn { margin-top: 14px; }
  .abn .label { color: var(--teal); }
</style>
</head>
<body>
  <section class="card card-front">
    <p class="brand-name">
      <span class="title">Velvet Bloom</span>
      <span class="tagline">Marisol's Cleaning Service</span>
    </p>
  </section>

  <section class="card card-back">
    <h1 class="contact-name">Marisol Denhart</h1>
    <p class="contact-role">Director</p>
    <div class="divider"></div>
    <p class="contact-line phone">
      <svg viewBox="0 0 24 24" aria-hidden="true"><path fill="#5ec7ca" d="M6.6 10.8a15 15 0 0 0 6.6 6.6l2.2-2.2a1 1 0 0 1 1-.25 11.4 11.4 0 0 0 3.6.57 1 1 0 0 1 1 1V20a1 1 0 0 1-1 1A17 17 0 0 1 3 4a1 1 0 0 1 1-1h3.5a1 1 0 0 1 1 1c0 1.25.2 2.45.57 3.57a1 1 0 0 1-.25 1z"/></svg>
      0418926547
    </p>
    <p class="contact-line email">
      <svg viewBox="0 0 24 24" aria-hidden="true"><rect x="2.5" y="5" width="19" height="14" fill="none" stroke="#5ec7ca" stroke-width="1.6"/><path d="M2.5 5l9.5 8 9.5-8M2.5 19l7-6.5M21.5 19l-7-6.5" fill="none" stroke="#5ec7ca" stroke-width="1.6"/></svg>
      marisolsvelvetcleaning@brightmail.example
    </p>
    <p class="contact-line abn"><span class="label">ABN :</span> 47193062857</p>
  </section>
</body>
</html>
```